Road Sign at our office 84 in X 48 in - Small Billboard

Kestrel Electrical
Electrical & Lighting Services

- we need a sign design for our small business/company based in Calhoun, GA called Kestrel Electrical - "our mission is to provide Northwest Georgia with dependable, high-quality electrical services that prioritize safety, integrity, and long-term reliability. As a woman-owned business with over 25 years of experience, we are committed to delivering exceptional workmanship and personalized service for every commercial, residential, and industrial project we undertake. We stand behind our work with a lifetime warranty—because your trust is our most powerful connection."

display logo, phone number, and open to other ideas without being cluttered, maybe instead of full website address, just use @kstelectrical and it will send them to all of our website and socials...

it needs to be easy to read as they drive down the road
this is a place where people may be traveling at high speeds, make sure it's easy to see and understand at a glance.
It will be hanging 20-24ft from the ground. Like a small billboard.

https://kstelectricalservices.example/

Industry/Entity Type

Electrical Contractor

Requirements
Nice to have
• match the look and feel of website and socials

```html
<!DOCTYPE html>
<html lang="en">
<head>
<meta charset="utf-8">
<title>Kestrel Electrical – Road Sign</title>
<link rel="stylesheet" href="https://fonts.googleapis.com/css2?family=Montserrat:wght@600;700;800;900&display=swap">
<style>
  :root {
    --page-bg: #ebebeb;
    --sign-white: #ffffff;
    --contact-grey: #e9e9e9;
    --ink: #111111;
    --flame: #f15a29;
    --amber: #f7941d;
    --highlight: #f9a11b;
    --photo-light: #cfc9bd;
    --photo-mid: #a9a59c;
    --photo-dark: #5a3a2e;
  }
  * { box-sizing: border-box; margin: 0; padding: 0; }
  html, body {
    width: 747px; height: 1200px; overflow: hidden;
    background: var(--page-bg);
    font-family: "Montserrat", Arial, sans-serif;
  }
  .canvas { position: relative; width: 747px; height: 1200px; }

  .sign {
    position: absolute; left: 23px; top: 400px;
    width: 700px; height: 400px;
    background: var(--sign-white);
    box-shadow: 0 14px 28px rgba(0,0,0,0.22);
    overflow: hidden;
  }

  .sign__photo {
    position: absolute; left: 0; top: 0; width: 297px; height: 400px;
    background: linear-gradient(90deg, var(--photo-dark) 0 4%, var(--photo-light) 12%, var(--photo-mid) 55%, var(--photo-light) 100%);
  }
  .sign__photo-frame { position: absolute; left: 0; top: 0; width: 297px; height: 400px; }

  .sign__band {
    position: absolute; left: 297px; top: 0; width: 15px; height: 400px;
    background: var(--amber);
  }
  .sign__band-arrow { position: absolute; left: 311px; top: 178px; }

  .sign__contact {
    position: absolute; left: 312px; top: 283px; width: 388px; height: 117px;
    background: var(--contact-grey);
  }

  .brand {
    position: absolute; left: 340px; top: 40px;
    display: flex; align-items: center; gap: 14px;
  }
  .brand__dot { width: 26px; height: 26px; border-radius: 50%; background: var(--flame); flex: none; }
  .brand__name {
    font-weight: 800; font-size: 40px; line-height: 44px;
    color: var(--ink); letter-spacing: -0.5px;
  }

  .headline {
    position: absolute; left: 343px; top: 172px;
    font-weight: 900; color: var(--ink); font-size: 26px; line-height: 30px;
    letter-spacing: -0.3px;
  }
  .headline__mark {
    display: inline-block; background: var(--highlight);
    padding: 0 8px; line-height: 28px;
  }
  .headline__line { display: block; }

  .services {
    position: absolute; left: 344px; top: 239px; width: 350px;
    color: var(--flame); font-weight: 600; font-size: 15.5px; line-height: 21px;
    white-space: nowrap;
  }

  .phone {
    position: absolute; left: 325px; top: 293px; width: 360px; height: 58px;
    background: var(--flame);
    border-radius: 22px 0 22px 0;
    color: #fff; font-weight: 800; font-size: 40px; line-height: 58px;
    text-align: center; letter-spacing: -0.5px;
  }

  .socials {
    position: absolute; left: 325px; top: 367px;
    display: flex; gap: 7px;
  }
  .socials__tile { width: 21px; height: 21px; border-radius: 5px; background: var(--ink); }

  .handle {
    position: absolute; right: 15px; top: 363px;
    font-weight: 800; font-size: 19px; line-height: 26px; color: var(--ink);
  }
</style>
</head>
<body>
<main class="canvas">
  <section class="sign" aria-label="Kestrel Electrical road sign">
    <div class="sign__photo" role="img" aria-label="Photo of two grey electrical panels with conduit on a corrugated metal wall"></div>
    <svg class="sign__photo-frame" viewBox="0 0 297 400" aria-hidden="true">
      <rect x="11" y="13" width="276" height="376" fill="none" stroke="#f15a29" stroke-width="0.6" opacity="0.8"/>
      <path d="M11 30 V13 H28 M270 13 H287 V30 M287 372 V389 H270 M28 389 H11 V372" fill="none" stroke="#f15a29" stroke-width="2"/>
    </svg>

    <div class="sign__band"></div>
    <svg class="sign__band-arrow" width="18" height="44" viewBox="0 0 18 44" aria-hidden="true">
      <polygon points="0,0 18,22 0,44" fill="#f7941d"/>
    </svg>

    <div class="sign__contact"></div>

    <div class="brand">
      <span class="brand__dot"></span>
      <span class="brand__name">Kestrel<br>Electrical</span>
    </div>

    <h1 class="headline">
      <span class="headline__line"><span class="headline__mark">HIGH-QUALITY</span></span>
      <span class="headline__line">ELECTRICAL SERVICES</span>
    </h1>

    <p class="services">ELECTRICAL - LIGHTING - COMMERCIAL<br>SECURITY - GENERATORS - AND MORE</p>

    <div class="phone">706-555-0148</div>

    <div class="socials" aria-label="Social channels">
      <span class="socials__tile"></span>
      <span class="socials__tile"></span>
      <span class="socials__tile"></span>
      <span class="socials__tile"></span>
    </div>
    <div class="handle">@kstelectrical</div>
  </section>
</main>
</body>
</html>
```